Kestra Rowe - Contact/Landing Page

I need a landing page which will essentially be the page that customers will go to from the 'website' link on TLX listing. It will provide a short overview of services which need to be selectable. a little further down can capture some contact details followed by a large Submit Now button etc...

I have some icon/logo's that can be utilised at the bottom of the page as industry type references.

Target Market(s)

End of Lease Cleaning Services

Industry/Entity Type

Cleaning Service

Colors

Designer to choose colors to be used in the design.

Requirements
Must have
• As per description
Should not have
• Colours to match my website kestrarowe.com.au

```html
<!DOCTYPE html>
<html lang="en">
<head>
<meta charset="utf-8">
<title>Kestra Rowe – End of Lease Services</title>
<link href="https://fonts.googleapis.com/css2?family=Oswald:wght@500;600&family=Montserrat:wght@400;500;600&family=Tinos&display=swap" rel="stylesheet">
<style>
:root{
  --blue:#0b75bd;
  --blue-dark:#0a6db3;
  --blue-light:#47aee3;
  --title:#3798d8;
  --ink:#222;
  --line:#d9d9d9;
  --grey-bg:#f4f5f7;
  --field-border:#dcdfe3;
  --placeholder:#444;
  --badge:#e3e7ec;
  --white:#fff;
}
*{box-sizing:border-box;margin:0;padding:0}
html,body{width:727px;height:1200px;overflow:hidden;background:var(--white)}
body{position:relative;font-family:"Montserrat",sans-serif;color:var(--ink)}
.abs{position:absolute}

/* header */
.hero-bg{left:0;top:0}
.contact{top:9px;display:flex;align-items:center;gap:7px;color:var(--white)}
.contact .icon-box{width:23px;height:23px;border:1px solid rgba(255,255,255,.7);background:var(--blue-light);display:flex;align-items:center;justify-content:center}
.contact .label{font-size:8.5px;line-height:11px}
.contact .value{font-size:9.5px;font-weight:500;line-height:12px;letter-spacing:.2px}
.contact-email{left:98px}
.contact-call{left:538px}
.brand{left:0;width:727px;top:82px;text-align:center;font-family:"Oswald",sans-serif;font-weight:600;color:#5cbaf0;font-size:46px;line-height:42px;letter-spacing:1px;text-transform:uppercase}
.brand-mark{left:352px;top:40px;width:22px;height:22px;border-radius:50%;background:#c3c7cc}
.hero-title{left:0;width:727px;top:206px;text-align:center;font-family:"Tinos",serif;font-weight:400;font-size:21.5px;color:var(--white);letter-spacing:.6px}

/* services */
.service{top:327px;width:158px;text-align:center}
.service svg{display:block}
.service h2{margin-top:13px;font-family:"Oswald",sans-serif;font-weight:500;font-size:18.5px;color:var(--title);letter-spacing:-.2px;line-height:22px}
.service p{margin-top:8px;font-size:8px;line-height:12.4px;height:38px;letter-spacing:.15px;white-space:nowrap}
.service .rule{margin-top:12px;border-top:1px solid var(--line)}
.service .select{margin-top:9px;font-size:7.5px;display:flex;justify-content:center;align-items:center;gap:5px}
.service .box{width:7px;height:7px;border:1px solid var(--title);border-radius:1px}

/* enquiry */
.grey-band{left:0;top:903px;width:727px;height:188px;background:var(--grey-bg)}
.photo{left:0;top:603px;width:402px;height:300px;background:linear-gradient(120deg,#f1f0ec 0%,#e4e4e1 40%,#cfd0ce 70%,#a8a39a 100%)}
.form-card{left:278px;top:697px;width:352px;height:236px;background:var(--white);box-shadow:0 6px 20px rgba(0,0,0,.07)}
.field{position:absolute;height:27px;border:1px solid var(--field-border);border-radius:2px;display:flex;align-items:center;gap:8px;padding-left:9px;font-size:7.5px;color:var(--placeholder);background:var(--white)}
.field svg{flex:none}
.field.tall{height:50px;align-items:flex-start;padding-top:9px}
.submit{position:absolute;left:22px;top:174px;width:93px;height:27px;border:none;border-radius:2px;background:linear-gradient(90deg,var(--blue-light),var(--blue-dark));color:var(--white);font-family:"Oswald",sans-serif;font-weight:500;font-size:14px;letter-spacing:.6px}

/* partners */
.partner{top:983px;width:99px;height:57px;background:var(--white);box-shadow:0 2px 8px rgba(0,0,0,.08);display:flex;align-items:center;justify-content:center}
.partner .badge{width:78px;height:30px;border-radius:3px;background:var(--badge)}

/* footer */
.footer{left:0;top:1091px;width:727px;height:109px;background:linear-gradient(90deg,#53b4e6 0%,#2f93d3 55%,#0b6fb6 100%);color:var(--white)}
.f-contact{top:26px;display:flex;align-items:center;gap:8px;font-size:8.8px}
.f-contact .circle{width:23px;height:23px;border-radius:50%;background:var(--white);display:flex;align-items:center;justify-content:center}
.f-contact strong{font-weight:600}
.f-rule{left:98px;top:64px;width:354px;border-top:1px solid rgba(255,255,255,.35)}
.copyright{left:98px;top:76px;font-size:7.6px;color:rgba(255,255,255,.9)}
.social{top:72px;width:17px;height:17px;border:1px solid var(--white);border-radius:50%}
.f-brand{left:558px;top:9px;width:68px;height:91px;background:var(--white);display:flex;flex-direction:column;align-items:center;justify-content:center;gap:6px;font-family:"Oswald",sans-serif;font-weight:600;color:#4aaee8;font-size:17px;line-height:16px;text-transform:uppercase;text-align:center}
.f-brand .dot{width:12px;height:12px;border-radius:50%;background:#c3c7cc}
</style>
</head>
<body>

<header>
  <svg class="abs hero-bg" width="727" height="300" viewBox="0 0 727 300" aria-hidden="true">
    <path d="M0 0H727V296Q363 216 0 296Z" fill="var(--blue)"/>
    <path d="M46 291Q363 238 663 291Q363 258 46 291Z" fill="#111"/>
  </svg>

  <div class="abs contact contact-email">
    <div class="icon-box">
      <svg width="13" height="10" viewBox="0 0 13 10"><rect x=".5" y=".5" width="12" height="9" fill="none" stroke="#fff"/><path d="M.5.5 6.5 5.5 12.5.5M.5 9.5 5 4.5M12.5 9.5 8 4.5" fill="none" stroke="#fff"/></svg>
    </div>
    <div><div class="label">Email</div><div class="value">info@kestrarowe.com.au</div></div>
  </div>

  <div class="abs contact contact-call">
    <div class="icon-box">
      <svg width="12" height="12" viewBox="0 0 12 12"><path d="M2.5 1 4.5 3.2 3.4 4.6Q4.6 7 7.2 8.4L8.6 7.3 10.8 9.4 9.4 11Q5 10.4 1 3Z" fill="#fff"/></svg>
    </div>
    <div><div class="label">Call / SMS</div><div class="value">0400 555 018</div></div>
  </div>

  <div class="abs brand-mark"></div>
  <div class="abs brand">Kestra<br>Rowe</div>
  <h1 class="abs hero-title">END OF LEASE SERVICES</h1>
</header>

<main>
  <section class="abs service" style="left:98px">
    <svg width="158" height="108" viewBox="0 0 158 108" role="img" aria-label="Photo of a cleaner wiping kitchen cupboards, framed in a house shape">
      <defs><linearGradient id="g1" x1="0" y1="0" x2="1" y2="1"><stop offset="0" stop-color="#f3f3f3"/><stop offset="1" stop-color="#c9ccd2"/></linearGradient></defs>
      <polygon points="79,0 146,47 126,47 126,102 30,102 30,47 12,47" fill="url(#g1)"/>
      <path d="M0 108Q79 94 158 108Q79 100 0 108Z" fill="#111"/>
    </svg>
    <h2>CLEANING</h2>
    <p>All Interior Cleaning Carried<br>Out To Property<br>Management Requirements.</p>
    <div class="rule"></div>
    <div class="select">Select <span class="box"></span></div>
  </section>

  <section class="abs service" style="left:285px">
    <svg width="158" height="108" viewBox="0 0 158 108" role="img" aria-label="Photo of a person vacuuming a carpet in a bright room, framed in a house shape">
      <defs><linearGradient id="g2" x1="0" y1="0" x2="0" y2="1"><stop offset="0" stop-color="#efeeeb"/><stop offset=".6" stop-color="#c9c2b8"/><stop offset="1" stop-color="#7c7770"/></linearGradient></defs>
      <polygon points="79,0 146,47 126,47 126,102 30,102 30,47 12,47" fill="url(#g2)"/>
      <path d="M0 108Q79 94 158 108Q79 100 0 108Z" fill="#111"/>
    </svg>
    <h2>CARPET CLEANING</h2>
    <p>Carpet Steam Cleaning to<br>Australian Standard<br>AS 3733:1995</p>
    <div class="rule"></div>
    <div class="select">Select <span class="box"></span></div>
  </section>

  <section class="abs service" style="left:472px">
    <svg width="158" height="108" viewBox="0 0 158 108" role="img" aria-label="Photo of a technician in a protective suit spraying for pests, framed in a house shape">
      <defs><linearGradient id="g3" x1="0" y1="0" x2="1" y2="0"><stop offset="0" stop-color="#d9dadb"/><stop offset=".6" stop-color="#eceded"/><stop offset="1" stop-color="#a77d55"/></linearGradient></defs>
      <polygon points="79,0 146,47 126,47 126,102 30,102 30,47 12,47" fill="url(#g3)"/>
      <path d="M0 108Q79 94 158 108Q79 100 0 108Z" fill="#111"/>
    </svg>
    <h2>PEST CONTROL</h2>
    <p>Mandatory<br>Requirement for pest on<br>Premises</p>
    <div class="rule"></div>
    <div class="select">Select <span class="box"></span></div>
  </section>

  <div class="abs grey-band"></div>
  <div class="abs photo" role="img" aria-label="Photo of hands typing on a laptop beside a green plant"></div>

  <form class="abs form-card">
    <div class="field" style="left:22px;top:35px;width:146px">
      <svg width="9" height="9" viewBox="0 0 9 9"><circle cx="4.5" cy="2.5" r="2.3" fill="var(--title)"/><path d="M0 9Q0 5 4.5 5Q9 5 9 9Z" fill="var(--title)"/></svg>First Name*
    </div>
    <div class="field" style="left:178px;top:35px;width:146px">
      <svg width="9" height="9" viewBox="0 0 9 9"><circle cx="4.5" cy="2.5" r="2.3" fill="var(--title)"/><path d="M0 9Q0 5 4.5 5Q9 5 9 9Z" fill="var(--title)"/></svg>Last Name*
    </div>
    <div class="field" style="left:22px;top:73px;width:146px">
      <svg width="9" height="9" viewBox="0 0 9 9"><path d="M0 4.5 9 0 6.5 9 4.3 5.2Z" fill="var(--title)"/></svg>Email*
    </div>
    <div class="field" style="left:178px;top:73px;width:146px">
      <svg width="9" height="9" viewBox="0 0 12 12"><path d="M2.5 1 4.5 3.2 3.4 4.6Q4.6 7 7.2 8.4L8.6 7.3 10.8 9.4 9.4 11Q5 10.4 1 3Z" fill="var(--title)"/></svg>Phone*
    </div>
    <div class="field tall" style="left:22px;top:111px;width:302px">
      <svg width="7" height="9" viewBox="0 0 7 9"><path d="M3.5 9Q0 5 0 3.5A3.5 3.5 0 0 1 7 3.5Q7 5 3.5 9Z" fill="var(--title)"/><circle cx="3.5" cy="3.4" r="1.3" fill="#fff"/></svg>Suburb*
    </div>
    <button class="submit" type="submit">SUBMIT</button>
  </form>

  <div class="abs partner" style="left:98px" role="img" aria-label="Industry accreditation badge"><span class="badge"></span></div>
  <div class="abs partner" style="left:206px" role="img" aria-label="Industry accreditation badge"><span class="badge"></span></div>
  <div class="abs partner" style="left:314px" role="img" aria-label="Industry accreditation badge"><span class="badge"></span></div>
  <div class="abs partner" style="left:422px" role="img" aria-label="Industry accreditation badge"><span class="badge"></span></div>
  <div class="abs partner" style="left:530px" role="img" aria-label="Industry accreditation badge"><span class="badge"></span></div>
</main>

<footer class="abs footer">
  <div class="abs f-contact" style="left:98px">
    <span class="circle"><svg width="12" height="9" viewBox="0 0 13 10"><rect x=".5" y=".5" width="12" height="9" fill="none" stroke="var(--title)"/><path d="M.5.5 6.5 5.5 12.5.5" fill="none" stroke="var(--title)"/></svg></span>
    <span><strong>Email :</strong> info@kestrarowe.com.au</span>
  </div>
  <div class="abs f-contact" style="left:302px">
    <span class="circle"><svg width="11" height="11" viewBox="0 0 12 12"><path d="M2.5 1 4.5 3.2 3.4 4.6Q4.6 7 7.2 8.4L8.6 7.3 10.8 9.4 9.4 11Q5 10.4 1 3Z" fill="var(--title)"/></svg></span>
    <span><strong>CALL :</strong> 0400 555 018</span>
  </div>
  <div class="abs f-rule"></div>
  <div class="abs copyright">Copyright © 2021 KESTRA ROWE. All Rights Reserved.</div>
  <span class="abs social" style="left:367px"></span>
  <span class="abs social" style="left:390px"></span>
  <span class="abs social" style="left:413px"></span>
  <div class="abs f-brand"><span class="dot"></span>Kestra<br>Rowe</div>
</footer>

</body>
</html>
```